PowerPoint template for Credit Card Processor

We need a powerpoint template for our new credit card processing company. Our goal is to sign up merchants to accept credit cards. We will be making presentations to merchants to get them to sign up for our services.

We already have a logo designed. We'd like to incorporate that logo and color scheme in the powerpoint template. The logo file is an illustrator file.

I generally like light colored backgrounds. Nothing too dark.

Credit Card

• our logo

```html
<!DOCTYPE html>
<html lang="en">
<head>
<meta charset="utf-8">
<title>Merchant Services Slide Template</title>
<link href="https://fonts.googleapis.com/css2?family=Roboto:wght@400;700;900&display=swap" rel="stylesheet">
<style>
  :root {
    --stage: #d9d9d7;
    --navy: #0b4a7e;
    --ocean: #1a7fb5;
    --cyan: #22c0ef;
    --cyan-pale: #8fdcf5;
    --steel-light: #c9cccf;
    --steel-dark: #8d9196;
    --white: #ffffff;
  }
  * { margin: 0; padding: 0; box-sizing: border-box; }
  html, body {
    width: 1200px; height: 803px; overflow: hidden;
    background: var(--stage);
    font-family: "Roboto", Arial, sans-serif;
  }
  .slide {
    position: absolute; left: 80px; top: 109px;
    width: 1040px; height: 585px; overflow: hidden;
    box-shadow: 0 10px 30px rgba(0,0,0,0.25);
  }
  .slide-backdrop { position: absolute; inset: 0; width: 100%; height: 100%; }
  .slide-title {
    position: absolute; left: 34px; top: 160px;
    font-size: 36px; font-weight: 900; letter-spacing: -0.5px;
    color: var(--white);
    text-shadow: 1px 2px 3px rgba(0,0,0,0.35);
  }
  .point-list {
    position: absolute; left: 62px; top: 228px; width: 350px;
    list-style: none; color: var(--white);
    font-size: 22px; font-weight: 400; line-height: 22px;
  }
  .point-list li { position: relative; padding-left: 24px; margin-bottom: 14px; }
  .point-list .point-marker { position: absolute; left: 0; top: 5px; width: 14px; height: 12px; }
  .body-copy {
    position: absolute; left: 515px; top: 150px; width: 495px;
    color: var(--white); font-size: 17px; font-weight: 700; line-height: 32.5px;
    text-shadow: 1px 2px 3px rgba(0,0,0,0.55);
  }
  .brand-name {
    position: absolute; left: 34px; top: 500px;
    display: flex; align-items: center; gap: 8px;
    color: var(--white); font-size: 22px; font-weight: 400;
  }
  .brand-dot { width: 18px; height: 18px; border-radius: 50%; background: var(--cyan-pale); }
</style>
</head>
<body>
<main class="slide">
  <svg class="slide-backdrop" viewBox="0 0 1040 585" preserveAspectRatio="none" aria-hidden="true">
    <defs>
      <linearGradient id="steel" x1="0" y1="0" x2="0" y2="1">
        <stop offset="0" stop-color="var(--steel-light)"/>
        <stop offset="1" stop-color="var(--steel-dark)"/>
      </linearGradient>
      <radialGradient id="deep" cx="0.3" cy="0.45" r="0.75">
        <stop offset="0" stop-color="var(--ocean)"/>
        <stop offset="1" stop-color="var(--navy)"/>
      </radialGradient>
    </defs>
    <rect class="steel-band" width="1040" height="140" fill="url(#steel)" role="img" aria-label="Brushed steel tread plate texture"/>
    <path class="wave-pale" d="M0,55 C140,140 300,140 470,80 S820,15 1040,55 V585 H0Z" fill="var(--cyan-pale)"/>
    <path class="wave-cyan" d="M0,75 C150,145 300,140 470,82 S820,22 1040,60 V585 H0Z" fill="var(--cyan)"/>
    <path class="field-deep" d="M0,98 C150,160 310,150 480,100 S830,55 1040,105 V585 H0Z" fill="url(#deep)"/>
    <path class="wave-foot-pale" d="M0,455 C120,500 200,520 260,520 V585 H0Z" fill="var(--cyan-pale)"/>
    <path class="wave-foot-cyan" d="M0,480 C200,530 380,440 580,450 S900,510 1040,515 V585 H0Z" fill="var(--cyan)"/>
    <path class="wave-foot-deep" d="M0,515 C200,555 400,480 610,490 S900,545 1040,550 V585 H0Z" fill="var(--navy)"/>
  </svg>

  <h1 class="slide-title">Lorem ipsum dolor sit</h1>

  <ul class="point-list">
    <li><svg class="point-marker" viewBox="0 0 14 12" aria-hidden="true"><path d="M0,0 L6,6 L0,12Z M7,0 L13,6 L7,12Z" fill="var(--white)"/></svg>Amet, consectetur adipisicing elit, sed do eiusmod tempor.</li>
    <li><svg class="point-marker" viewBox="0 0 14 12" aria-hidden="true"><path d="M0,0 L6,6 L0,12Z M7,0 L13,6 L7,12Z" fill="var(--white)"/></svg>Incididunt ut labore et dolore magna aliqua.</li>
    <li><svg class="point-marker" viewBox="0 0 14 12" aria-hidden="true"><path d="M0,0 L6,6 L0,12Z M7,0 L13,6 L7,12Z" fill="var(--white)"/></svg>Ut enim ad minim veniam, quis nostrud exercitation ullamco laboris nisi ut aliquip.</li>
  </ul>

  <p class="body-copy">Lorem ipsum dolor sit amet, consectetur adipisicing elit, sed do eiusmod tempor incididunt ut labore et dolore magna aliqua. Ut enim ad minim veniam, quis nostrud exercitation ullamco laboris nisi ut aliquip ex ea commodo consequat. Duis aute irure dolor in reprehenderit in voluptate velit esse cillum dolore eu fugiat nulla pariatur. Excepteur sint occaecat cupidatat non proident, sunt in culpa qui officia deserunt mollit anim id est laborum.</p>

  <div class="brand-name"><span class="brand-dot"></span>ClearSwipe.net</div>
</main>
</body>
</html>
```